Billboard design for high performance real estate broker

I need a new design for a billboard representing my Real Estate Company. The company name is Maribel Toft Real Estate. I want to include my photo. Other necessary items are my phone number :
512.804.6671 along with Homekeyer brand logo and Open Dwelling logo. I will send my photos (you and choose whichever works best and you can crop as needed) and my current company logo, but I am open to changes on that item. I need a good tag line on the billboard. It is located on a busy street so I don’t need a lot of text in the tag line. I think you can probably get the homekeyer brand logo and open dwelling logo online. If not, I can send them. I have been in the industry almost 20 years so I am very experienced. I represent buyers and sellers. Most of my clients are repeat clients and referrals. Just trying to stay top of mind for anyone wanting to buy or sell real estate. I handle residential, land and some commercial sales.

Target Market(s)

Could be first time homebuyer or someone looking for buy or sell their luxury home

Industry/Entity Type

Real Estate

Colors
0054AA
0677BA
7BADD7
CADEEF
E8F1F8

Requirements
Must have
• Attention getting with catchy tag line
Nice to have
• Nice pop to catch drivers attention
Should not have
• Not too much wording as the viewer will be speeding by the sign

```html
<!DOCTYPE html>
<html lang="en">
<head>
<meta charset="utf-8">
<title>Maribel Toft Real Estate Billboard</title>
<link href="https://fonts.googleapis.com/css2?family=Cinzel:wght@400&family=Libre+Baskerville:wght@700&family=Montserrat:wght@500;800&display=swap" rel="stylesheet">
<style>
  :root {
    --page-bg: #dcdcde;
    --sky-pale: #d6eef6;
    --sky-mid: #b1e1f7;
    --stripe-white: #f3fafd;
    --navy: #1f3769;
    --white: #ffffff;
    --photo-top: #e4c98e;
    --photo-bottom: #3a63c4;
  }
  html, body {
    margin: 0;
    padding: 0;
    width: 1200px;
    height: 1120px;
    overflow: hidden;
    background: var(--page-bg);
  }
  .billboard {
    position: absolute;
    left: 30px;
    top: 394px;
    width: 1140px;
    height: 332px;
    overflow: hidden;
    background: var(--sky-pale);
  }
  .billboard-backdrop {
    position: absolute;
    inset: 0;
  }
  .brand-name {
    position: absolute;
    left: 260px;
    top: 52px;
    width: 320px;
    text-align: center;
    font-family: "Libre Baskerville", serif;
    font-weight: 700;
    color: var(--navy);
    font-size: 25px;
    line-height: 1.15;
  }
  .brand-name .brand-mark {
    display: inline-block;
    width: 12px;
    height: 12px;
    border-radius: 50%;
    background: var(--navy);
    margin-right: 8px;
    vertical-align: middle;
  }
  .brand-name .brand-sub {
    display: block;
    font-size: 19px;
  }
  .tagline {
    position: absolute;
    left: 118px;
    top: 146px;
    width: 600px;
    margin: 0;
    text-align: center;
    font-family: "Cinzel", serif;
    font-weight: 400;
    color: var(--navy);
    font-size: 43px;
    line-height: 44px;
    letter-spacing: 1px;
  }
  .contact-band {
    position: absolute;
    left: 0;
    top: 259px;
    width: 1140px;
    height: 73px;
    background: var(--navy);
  }
  .phone {
    position: absolute;
    left: 74px;
    top: 8px;
    font-family: "Montserrat", sans-serif;
    font-weight: 800;
    font-size: 50px;
    line-height: 56px;
    color: var(--white);
    letter-spacing: 1px;
  }
  .band-divider {
    position: absolute;
    left: 480px;
    top: 13px;
    width: 2px;
    height: 46px;
    background: var(--white);
  }
  .website {
    position: absolute;
    left: 503px;
    top: 18px;
    font-family: "Montserrat", sans-serif;
    font-weight: 500;
    font-size: 27px;
    line-height: 34px;
    color: var(--white);
  }
  .agent-photo {
    position: absolute;
    left: 778px;
    top: 14px;
    width: 282px;
    height: 318px;
    border-radius: 130px 130px 0 0;
    background: linear-gradient(180deg, var(--photo-top) 0%, var(--photo-top) 40%, var(--photo-bottom) 75%);
  }
  .badges {
    position: absolute;
    right: 14px;
    top: 290px;
    display: flex;
    gap: 12px;
  }
  .badge {
    width: 18px;
    height: 18px;
    background: var(--white);
  }
</style>
</head>
<body>
  <main class="billboard">
    <svg class="billboard-backdrop" width="1140" height="332" viewBox="0 0 1140 332" aria-hidden="true">
      <defs>
        <linearGradient id="skyFade" x1="0" y1="0" x2="1" y2="0">
          <stop offset="0" stop-color="#d6eef6"/>
          <stop offset="1" stop-color="#b1e1f7"/>
        </linearGradient>
      </defs>
      <polygon points="610,0 1140,0 1140,332 430,332" fill="url(#skyFade)"/>
      <polygon points="850,0 988,0 808,259 675,259" fill="#f3fafd"/>
      <polygon points="1140,40 1140,250 1040,332 1000,332" fill="#cfeefb"/>
      <polygon points="1140,80 1140,332 1060,332" fill="#eef8fc"/>
    </svg>

    <div class="brand-name">
      <span class="brand-mark"></span>Maribel Toft
      <span class="brand-sub">Real Estate</span>
    </div>

    <h1 class="tagline">Buy Land, They're Not<br>Making It Anymore</h1>

    <div class="contact-band">
      <div class="phone">512.804.6671</div>
      <div class="band-divider"></div>
      <div class="website">maribeltoft.com</div>
      <div class="badges">
        <span class="badge" aria-label="Homekeyer badge"></span>
        <span class="badge" aria-label="Open Dwelling badge"></span>
      </div>
    </div>

    <div class="agent-photo" role="img" aria-label="Portrait photo of the agent, smiling, blonde hair, royal blue blouse"></div>
  </main>
</body>
</html>
```